Brightvantage.com tech company website

Current site is www.brightvantage.com. The site will tell you about our company.

Designs we like are:
http://megainfo.quellorix.com
www.trelvo.com
www.morvasket.com

Target Market(s)

B2B

Industry/Entity Type

It Company

Coding

Coded - Design and coding required

Number of Pages Required

5+ page

Requirements
Must have
• We want to entice without giving away too much info. We like graphics and colors. But website must look official and credible.

```html
<!DOCTYPE html>
<html lang="en">
<head>
<meta charset="utf-8">
<title>Brightvantage</title>
<link rel="stylesheet" href="https://fonts.googleapis.com/css2?family=Marcellus&family=Open+Sans:wght@400;600;700&display=swap">
<style>
:root{
  --blue:#1f5d92;
  --blue-dark:#17476f;
  --blue-light:#3b86c4;
  --navy:#1b3d5f;
  --grey-band:#8a8987;
  --grey-dark:#4a4a4a;
  --text:#4d4d4d;
  --white:#ffffff;
  --page:#ffffff;
}
*{box-sizing:border-box;margin:0;padding:0}
html,body{width:1200px;height:2900px;overflow:hidden;background:var(--page)}
body{font-family:"Open Sans",Arial,sans-serif;color:var(--text);position:relative}
.header{position:absolute;top:0;left:0;width:1200px;height:100px;background:var(--white)}
.brand{position:absolute;left:60px;top:30px;display:flex;align-items:center;gap:12px;font:700 34px "Open Sans",Arial,sans-serif;color:var(--blue)}
.brand-mark{width:30px;height:30px;background:var(--blue)}
.nav{position:absolute;right:60px;top:42px;display:flex;gap:26px;font-size:14px;color:#555}
.nav .active{color:var(--blue);border-bottom:2px solid var(--blue);padding-bottom:4px}
.hero{position:absolute;top:100px;left:0;width:1200px;height:660px;background:linear-gradient(110deg,#2d78b5 0%,#4f97cf 55%,#2a6aa3 100%)}
.hero-photo{position:absolute;right:0;top:0;width:520px;height:660px;background:linear-gradient(160deg,#9fc6e3 0%,#6f9fc7 60%,#3e7bb0 100%)}
.hero-title{position:absolute;left:70px;top:300px;font:400 44px "Open Sans",Arial,sans-serif;color:var(--white)}
.hero-sub{position:absolute;left:60px;top:370px;width:520px;padding:16px 18px;background:rgba(20,60,100,.55);color:var(--white);font-size:16px;line-height:1.5}
.arrow{position:absolute;top:270px;color:var(--white);font-size:40px}
.dots{position:absolute;top:725px;left:0;width:1200px;display:flex;justify-content:center;gap:12px}
.dots span{width:14px;height:14px;border-radius:50%;border:2px solid var(--white)}
.dots .on{background:var(--white)}
.section-title{position:absolute;left:0;width:1200px;text-align:center;font:400 44px "Marcellus",serif;color:var(--blue)}
.lead{position:absolute;left:260px;width:680px;text-align:center;font-size:15px;line-height:1.6}
.btn{position:absolute;left:500px;width:200px;height:46px;background:var(--blue);color:var(--white);font-size:18px;text-align:center;line-height:46px}
.band{position:absolute;left:0;width:1200px;height:240px}
.band.grey{background:var(--grey-band)}
.band.navy{background:var(--navy)}
.band h3{position:absolute;font:400 28px "Marcellus",serif;color:var(--white)}
.band p{position:absolute;width:500px;font-size:14px;line-height:1.55;color:var(--white)}
.band .photo{position:absolute;top:30px;width:360px;height:180px}
.cases{position:absolute;top:2085px;left:70px;display:flex;gap:22px}
.case{width:168px;height:118px;border:1px solid #c8c8c8;background:#f4f4f4;font-size:13px;line-height:1.4;text-align:center;padding:18px 10px;color:#555}
.case.on{background:var(--blue);color:var(--white);border-color:var(--blue)}
.contact{position:absolute;top:2270px;left:0;width:1200px;height:580px;background:var(--grey-dark)}
.map{position:absolute;right:0;top:0;width:520px;height:580px;background:linear-gradient(135deg,#d9d4c2,#c5cfb8 50%,#cbd7e4)}
.contact h2{position:absolute;left:0;width:680px;top:30px;text-align:center;font:400 54px "Marcellus",serif;color:var(--white)}
.contact .tag{position:absolute;left:0;width:680px;top:105px;text-align:center;font-size:14px;color:#ddd}
.field{position:absolute;left:160px;width:360px;height:28px;background:var(--white);font-size:12px;color:#777;padding:6px 10px}
.submit{position:absolute;left:270px;top:355px;width:140px;height:40px;border:2px solid var(--white);color:var(--white);text-align:center;line-height:36px;font-size:16px}
.info{position:absolute;top:430px;font-size:13px;color:#eee;line-height:1.5;display:flex;gap:10px}
.social{position:absolute;left:520px;top:445px;display:flex;gap:8px}
.social span{width:36px;height:36px;border-radius:50%;background:var(--blue-light)}
.footer{position:absolute;top:2850px;left:0;width:1200px;height:50px;background:var(--navy);color:#ccc;font-size:13px;text-align:center;line-height:50px}
.footer b{color:var(--white)}
</style>
</head>
<body>
<header class="header">
  <div class="brand"><span class="brand-mark"></span>Brightvantage</div>
  <nav class="nav"><span class="active">Home</span><span>About</span><span>Big Data &amp; Analytics</span><span>Perception &amp; Influence</span><span>Case Studies</span><span>Contact Us</span></nav>
</header>

<section class="hero">
  <div class="hero-photo" role="img" aria-label="Photo of a smiling woman holding a tablet"></div>
  <span class="arrow" style="left:20px">&#8249;</span>
  <span class="arrow" style="right:20px">&#8250;</span>
  <h1 class="hero-title">existing capabilities, systems, &amp; services</h1>
  <p class="hero-sub">Brightvantage is expert at data collection and analysis, extracting the data important to business.</p>
</section>
<div class="dots"><span></span><span class="on"></span><span></span></div>

<h2 class="section-title" style="top:840px">Know About Brightvantage</h2>
<p class="lead" style="top:915px">Brightvantage was created to sell, to the commercial sector, existing capabilities, systems, and services, developed over the last decade for the US government security apparatus. Specific assignments involving Big Data gathering, enhancement and analytics, as well as perception.</p>
<div class="btn" style="top:1030px">What We Do</div>

<section class="band grey" style="top:1110px">
  <h3 style="left:70px;top:30px">Data Enhancement</h3>
  <p style="left:70px;top:85px">We will enhance your in-house data on a one-time, or ongoing basis to give you a complete picture of your customers, and identify their demographic and psychographic trigger points to allow you to service them better, and increase your closing ratios.</p>
  <div class="photo" style="right:90px;background:linear-gradient(135deg,#e8eef4,#aac3da)" role="img" aria-label="Photo of hands pointing at charts on a tablet"></div>
</section>

<section class="band navy" style="top:1370px">
  <div class="photo" style="left:90px;background:linear-gradient(135deg,#2b3440,#6a7888)" role="img" aria-label="Photo of a businessman's hands around a glowing security symbol"></div>
  <h3 style="left:520px;top:30px">Data Monetization</h3>
  <p style="left:520px;top:85px;width:600px">You're spending time and money generating new leads, and your cost per customer acquisition is directly tied to your closing ratio. We can turn the leads you didn't close into money, and in doing so, significantly lower your cost per customer acquisition.</p>
</section>

<section class="band grey" style="top:1630px">
  <h3 style="left:70px;top:30px">Business intelligence</h3>
  <p style="left:70px;top:85px">Information is plentiful; knowledge is power. We create algorithms to automatically comb the web for relevant information about your competitors, customers, and stakeholders. We enable all the data to expose a clear picture of what's really going on.</p>
  <div class="photo" style="right:90px;background:linear-gradient(135deg,#f0f0f0,#b9c4cf)" role="img" aria-label="Photo of a business team joining hands"></div>
</section>
<div class="btn" style="top:1890px;left:470px;width:260px">This Are Our Services</div>

<h2 class="section-title" style="top:1970px">Our Case Study</h2>
<p class="lead" style="top:2030px;left:330px;width:540px;font-size:13px">The following are actual case studies from real clients. Click on any case study below to find out more details.</p>
<div class="cases">
  <div class="case on">Maintained share value for fortune 500 Company under regulatory duress</div>
  <div class="case">Initial Public Offering Management for Financial Services Co.</div>
  <div class="case">Increased sales with our Data Targeting Marketing service</div>
  <div class="case">Customized solution for increased leads and revenue for startup</div>
  <div class="case">Risk Characterization for Supply Chains</div>
  <div class="case">Minimized reputational risk and enhanced sentiment for high profile family</div>
</div>

<section class="contact">
  <div class="map" role="img" aria-label="Street map of the office area"></div>
  <h2>Contact Me</h2>
  <p class="tag">Keep In Touch With Us</p>
  <div class="field" style="top:150px">Name</div>
  <div class="field" style="top:188px">Email ID</div>
  <div class="field" style="top:226px;height:110px">Message</div>
  <div class="submit">Submit</div>
  <div class="info" style="left:60px;width:200px">
    <svg width="16" height="22" viewBox="0 0 16 22"><path d="M8 0a8 8 0 0 1 8 8c0 6-8 14-8 14S0 14 0 8a8 8 0 0 1 8-8z" fill="#fff"/><circle cx="8" cy="8" r="3" fill="#4a4a4a"/></svg>
    <span>Lorem Ipsum is simply dummy text of the printing</span>
  </div>
  <div class="info" style="left:300px;flex-direction:column;gap:6px">
    <span>&#9742; 555 014 2200</span>
    <span>&#9993; info@brightvantage.com</span>
  </div>
  <div class="social"><span></span><span></span><span></span></div>
</section>

<footer class="footer">Copyright <b>Brightvantage</b> 2014</footer>
</body>
</html>
```